Brinmoor Logistics - Cards and Logo

We need a logo and card design for a Logistics company located in Chicago. Our competitors are KRV and Torvan. We would like to see designs that incorporate a logo that shows all ways in terms of direction. The colors would be Electric Blue, Grays, Blacks and White. I like how Pumo has a badge type logo that is strong and clean. Quorvel also has a strong font that is futuristic. The final design should communicate we are a strong and technological type of company. I show a picture of the colors we like from a pumo cooler.

```html
<!DOCTYPE html>
<html lang="en">
<head>
<meta charset="utf-8">
<title>Brinmoor Logistics – Business Card</title>
<link href="https://fonts.googleapis.com/css2?family=Montserrat:wght@600;700;800&display=swap" rel="stylesheet">
<style>
  :root {
    --stage: #010b18;
    --card: #0e0f11;
    --blue: #0fa6e0;
    --blue-deep: #1a7fd0;
    --gray: #a7a6a4;
    --gray-text: #b4b4b4;
    --map: #1f3a36;
  }
  * { margin: 0; padding: 0; box-sizing: border-box; }
  html, body { width: 1200px; height: 1000px; overflow: hidden; }
  body {
    background: var(--stage);
    font-family: "Montserrat", sans-serif;
    position: relative;
  }
  .card {
    position: absolute;
    left: 260px;
    width: 683px;
    height: 390px;
    background: var(--card);
    overflow: hidden;
  }
  .card--front { top: 87px; }
  .card--back { top: 517px; }

  .world-map {
    position: absolute;
    left: 50px; top: 8px;
    width: 590px; height: 370px;
    background: radial-gradient(ellipse at 50% 45%, rgba(38,70,64,.55), rgba(31,58,54,.25) 55%, rgba(14,15,17,0) 75%);
  }
  .brand-name {
    position: absolute;
    color: var(--blue);
    font-weight: 800;
    text-transform: uppercase;
    white-space: nowrap;
    letter-spacing: 1px;
  }
  .card--front .brand-name {
    left: 0; right: 0; top: 172px;
    text-align: center;
    font-size: 42px;
  }
  .card--back .brand-name {
    left: 30px; top: 62px;
    font-size: 30px;
  }

  .person-name {
    position: absolute;
    right: 44px; top: 152px;
    font-size: 27px; font-weight: 700;
    color: var(--gray);
    letter-spacing: 1px;
  }
  .name-dash {
    position: absolute;
    left: 645px; top: 166px;
    width: 24px; height: 5px;
    background: var(--blue);
  }
  .divider {
    position: absolute;
    left: 18px; top: 197px;
    width: 531px; height: 5px;
    background: var(--gray);
  }
  .person-role {
    position: absolute;
    left: 557px; top: 189px;
    font-size: 19px; font-weight: 700;
    color: var(--blue);
  }

  .contact {
    position: absolute;
    display: flex;
    align-items: flex-start;
    gap: 12px;
    font-size: 18px; font-weight: 700;
    color: var(--gray-text);
    line-height: 23px;
  }
  .contact__icon {
    width: 32px; height: 32px;
    border-radius: 3px;
    background: linear-gradient(180deg, #1fb4ec, var(--blue-deep));
    flex: none;
  }
  .contact__text { padding-top: 4px; }
  .contact--phone { left: 29px; top: 223px; }
  .contact--email { left: 29px; top: 269px; }
  .contact--web { left: 29px; top: 315px; }
  .contact--address { left: 366px; top: 269px; }

  .footer-band { position: absolute; left: 0; bottom: 0; width: 683px; height: 25px; }
</style>
</head>
<body>

<section class="card card--front">
  <div class="world-map" role="img" aria-label="Dotted world map in dark teal behind the brand name"></div>
  <div class="brand-name">Brinmoor Logistics</div>
</section>

<section class="card card--back">
  <div class="brand-name">Brinmoor Logistics</div>

  <div class="person-name">JOHN DOE</div>
  <div class="name-dash"></div>
  <div class="divider"></div>
  <div class="person-role">Owner</div>

  <div class="contact contact--phone">
    <svg class="contact__icon" viewBox="0 0 32 32"><rect width="32" height="32" rx="3" fill="#1497dc"/><rect x="11" y="7" width="10" height="18" rx="1.5" fill="none" stroke="#0e0f11" stroke-width="2"/><circle cx="16" cy="22" r="1" fill="#0e0f11"/></svg>
    <span class="contact__text">123.456.7890</span>
  </div>
  <div class="contact contact--email">
    <svg class="contact__icon" viewBox="0 0 32 32"><rect width="32" height="32" rx="3" fill="#1497dc"/><rect x="7" y="10" width="18" height="12" fill="none" stroke="#0e0f11" stroke-width="2"/><path d="M7 10l9 7 9-7M7 22l7-6M25 22l-7-6" fill="none" stroke="#0e0f11" stroke-width="1.8"/></svg>
    <span class="contact__text">brinmoorlogistics@info.com</span>
  </div>
  <div class="contact contact--web">
    <svg class="contact__icon" viewBox="0 0 32 32"><rect width="32" height="32" rx="3" fill="#1497dc"/><circle cx="16" cy="16" r="9" fill="none" stroke="#0e0f11" stroke-width="2"/><ellipse cx="16" cy="16" rx="4" ry="9" fill="none" stroke="#0e0f11" stroke-width="1.6"/><path d="M7 16h18M9 11h14M9 21h14" stroke="#0e0f11" stroke-width="1.4"/></svg>
    <span class="contact__text">www.brinmoorlogistics.com</span>
  </div>
  <div class="contact contact--address">
    <svg class="contact__icon" viewBox="0 0 32 32"><rect width="32" height="32" rx="3" fill="#1497dc"/><path d="M16 26s-7-8-7-13a7 7 0 0 1 14 0c0 5-7 13-7 13z" fill="#0e0f11"/><circle cx="16" cy="13" r="2.6" fill="#1497dc"/></svg>
    <span class="contact__text">4820 W Harlan Ave<br>Chicago, IL 60644<br>United States</span>
  </div>

  <svg class="footer-band" viewBox="0 0 683 25" preserveAspectRatio="none">
    <defs>
      <linearGradient id="band-blue" x1="0" x2="1">
        <stop offset="0" stop-color="#05b0e6"/>
        <stop offset="1" stop-color="#1a7fd0"/>
      </linearGradient>
    </defs>
    <polygon points="0,0 118,0 132,25 0,25" fill="#a7a6a4"/>
    <polygon points="125,0 683,0 683,25 139,25" fill="url(#band-blue)"/>
  </svg>
</section>

</body>
</html>
```